Image Ads needed for a Pharmacy Education e-commerce website

I need image ads with these specifications:

Supported formats: JPG, PNG, GIF
File size: 3MB max
Recommended aspect ratios: 1:1 square; 4:5 portrait; 4:3 landscape; 16:9 landscape
Recommended resolutions: 1080x1080 square, 1080x1350 portrait, 1440x1080 landscape, 1920x1080 landscape
Thumbnail: Displays at 400x300 pixels
Thumbnail file size: 500KB max

```html
<!DOCTYPE html>
<html lang="en">
<head>
<meta charset="utf-8">
<title>Unlimited PEAC CEUs $39 – DoseWise</title>
<link href="https://fonts.googleapis.com/css2?family=Poppins:wght@700&display=swap" rel="stylesheet">
<style>
  :root {
    --green: #6a9f3f;
    --navy: #233a5a;
    --bg: #ffffff;
    --blob: #efefef;
    --coat: #f6f8fb;
    --scrub-light: #9cc0e6;
    --scrub: #1f6db3;
    --scrub-dark: #0f3f78;
    --stripe-1: #023e64;
    --stripe-2: #136a9e;
    --stripe-3: #6ca11e;
    --stripe-4: #e08c3a;
  }
  html, body {
    margin: 0;
    padding: 0;
    overflow: hidden;
  }
  .ad {
    position: relative;
    width: 1200px;
    height: 675px;
    background: var(--bg);
    overflow: hidden;
    font-family: "Poppins", sans-serif;
  }
  .headline {
    position: absolute;
    left: 60px;
    top: 18px;
    margin: 0;
    font-size: 86px;
    font-weight: 700;
    line-height: 1.2;
    letter-spacing: -0.5px;
    white-space: nowrap;
    color: var(--navy);
  }
  .headline .accent { color: var(--green); }
  .illustration {
    position: absolute;
    left: 420px;
    top: 150px;
    width: 780px;
    height: 525px;
  }
  .brand {
    position: absolute;
    left: 58px;
    top: 436px;
    display: flex;
    align-items: center;
    gap: 12px;
    font-size: 72px;
    font-weight: 700;
    color: var(--navy);
    line-height: 1;
    letter-spacing: -1px;
  }
  .brand-dot {
    width: 22px;
    height: 22px;
    border-radius: 50%;
    background: var(--green);
  }
  .stripe {
    position: absolute;
    left: 0;
    top: 631px;
    width: 1200px;
    height: 16px;
    display: flex;
  }
  .stripe span { flex: 1; }
  .stripe span:nth-child(1) { background: var(--stripe-1); }
  .stripe span:nth-child(2) { background: var(--stripe-2); }
  .stripe span:nth-child(3) { background: var(--stripe-3); }
  .stripe span:nth-child(4) { background: var(--stripe-4); }
</style>
</head>
<body>
  <main class="ad">
    <h1 class="headline"><span class="accent">Unlimited</span> PEAC Ceus $39</h1>

    <svg class="illustration" role="img" aria-label="Illustration of a group of five pharmacists and healthcare workers in white coats and blue scrubs standing together" viewBox="0 0 780 525">
      <defs>
        <linearGradient id="team-tones" x1="0" y1="0" x2="0" y2="1">
          <stop offset="0" stop-color="var(--coat)"/>
          <stop offset="0.45" stop-color="#dbe6f3"/>
          <stop offset="0.75" stop-color="var(--scrub-light)"/>
          <stop offset="1" stop-color="var(--scrub)"/>
        </linearGradient>
        <linearGradient id="team-side" x1="0" y1="0" x2="1" y2="0">
          <stop offset="0" stop-color="var(--scrub-dark)" stop-opacity="0.18"/>
          <stop offset="0.5" stop-color="var(--scrub-dark)" stop-opacity="0"/>
          <stop offset="1" stop-color="var(--scrub-dark)" stop-opacity="0.22"/>
        </linearGradient>
      </defs>
      <path class="backdrop" d="M40 170 C60 60 220 20 420 40 C560 55 700 -10 780 30 L780 525 L40 525 C10 430 20 260 40 170 Z" fill="var(--blob)"/>
      <rect class="team-area" x="55" y="20" width="725" height="461" rx="60" fill="url(#team-tones)"/>
      <rect class="team-area-shade" x="55" y="20" width="725" height="461" rx="60" fill="url(#team-side)"/>
    </svg>

    <div class="brand">
      <span>DoseWise</span>
      <span class="brand-dot"></span>
    </div>

    <div class="stripe" aria-hidden="true">
      <span></span><span></span><span></span><span></span>
    </div>
  </main>
</body>
</html>
```